Simple Modern Label for a Coconut oil product

We need a label designed for Organic Coconut oil. We would like the label to convey the gourmet/high quality product. It should be modern and simple and look like an artisinal product. The label will need to contain all the basic label requirements - Independence list, place for nutrition facts, our company logo etc.
The label will ultimately be printed as oil proof, so it will have a glossy appearance.
I have includes some examples that I like and a file with the logo.

Product Container - Wide Mount Clear Glass Jar: 4.75 inches tall (base to the bottom of the lid) and 9.5 in circumference
Label: Can be 1 or 2 separate labels, round, square and rectangle are okay
No larger than 3 inches high and 9 inches long

Target Market(s)

Middle Age home chef

Industry/Entity Type

Product

Requirements
Must have
• - logo (Attached below, I have this in multiple formats, let me know if you need them)
• - 14 FL OZ (414mL)
• - ingredient: organic unrefined whole kernel virgin coconut oil,
• - Manufacturer: XXX Y St., anywhere, CA, 99999
• - Distributed by Fernvale Naturals, P.O. Box 5521, Oakland, CA 94610 www.FernvaleNaturals.example
• - Certified Organic by Company Name
• - Product of Sri Lanka
Nice to have
• - Nutrition Facts
Should not have
• Clutter

```html
<!DOCTYPE html>
<html lang="en">
<head>
<meta charset="utf-8">
<title>Fernvale Naturals – Virgin Coconut Oil Label</title>
<link href="https://fonts.googleapis.com/css2?family=Jost:wght@300;400;500&display=swap" rel="stylesheet">
<style>
  :root {
    --navy: #062448;
    --mustard: #d3ae2b;
    --sunflower: #f3c915;
    --ice-blue: #d2e9f2;
    --white: #ffffff;
    --husk-dark: #6b4a30;
    --husk-light: #a88468;
    --page: #ffffff;
  }
  html, body {
    margin: 0;
    padding: 0;
    width: 1200px;
    height: 466px;
    overflow: hidden;
    background: var(--page);
  }
  .label {
    position: relative;
    width: 1200px;
    height: 466px;
    font-family: "Jost", "Futura", sans-serif;
  }
  .label-shapes {
    position: absolute;
    inset: 0;
  }
  .brand-name {
    position: absolute;
    left: 110px;
    top: 166px;
    display: flex;
    align-items: center;
    gap: 8px;
    color: var(--white);
    font-weight: 500;
    font-size: 21px;
    letter-spacing: 0.5px;
    text-transform: uppercase;
    white-space: nowrap;
  }
  .brand-mark {
    width: 16px;
    height: 16px;
    background: var(--white);
  }
  .product-name {
    position: absolute;
    left: 430px;
    width: 660px;
    top: 128px;
    margin: 0;
    text-align: center;
    color: var(--ice-blue);
    font-weight: 300;
    font-size: 72px;
    line-height: 1;
    letter-spacing: 0.5px;
  }
  .net-volume {
    position: absolute;
    left: 430px;
    width: 660px;
    top: 257px;
    margin: 0;
    text-align: center;
    color: var(--white);
    font-weight: 300;
    font-size: 27px;
    line-height: 1;
  }
</style>
</head>
<body>
<div class="label">
  <svg class="label-shapes" width="1200" height="466" viewBox="0 0 1200 466">
    <defs>
      <clipPath id="label-outline">
        <rect x="36" y="44" width="1130" height="376" rx="188" ry="188"/>
      </clipPath>
      <linearGradient id="spoon-fill" x1="0" y1="0" x2="0" y2="466" gradientUnits="userSpaceOnUse">
        <stop offset="0.497" stop-color="var(--mustard)"/>
        <stop offset="0.497" stop-color="var(--sunflower)"/>
      </linearGradient>
      <linearGradient id="illustration-tone" x1="0" y1="0" x2="1" y2="1">
        <stop offset="0" stop-color="var(--husk-light)"/>
        <stop offset="1" stop-color="var(--husk-dark)"/>
      </linearGradient>
    </defs>

    <g clip-path="url(#label-outline)">
      <rect class="label-base" x="36" y="44" width="1130" height="376" fill="var(--navy)"/>
      <path class="spoon-band" fill="url(#spoon-fill)"
        d="M216 76
           A156 156 0 0 1 362 176
           C385 212 440 224 560 227
           L960 229
           C1060 228 1120 217 1180 214
           L1180 246
           C1120 244 1060 238 960 236
           L560 238
           C440 240 392 256 366 296
           A156 156 0 1 1 216 76 Z"/>
    </g>

    <rect class="stitch-border" x="50" y="58" width="1102" height="348" rx="174" ry="174"
      fill="none" stroke="var(--white)" stroke-width="2.4" stroke-dasharray="2.4 3.6" stroke-linecap="round"/>

    <rect class="coconut-illustration" role="img"
      aria-label="Illustration area: whole coconut and halved coconut with a palm frond"
      x="102" y="206" width="206" height="170" rx="14" ry="14"
      fill="url(#illustration-tone)" opacity="0.85"/>
  </svg>

  <div class="brand-name"><span class="brand-mark"></span>Fernvale Naturals</div>

  <h1 class="product-name">Virgin Coconut Oil</h1>
  <p class="net-volume">14 FL OZ (414mL)</p>
</div>
</body>
</html>
```